Business Card for Mortuary

We need a business card design for our mortuary. We are not the "traditional" mortuary and specialize in simple cremations and burials. We use a two sided card.

Industry/Entity Type

Funeral Home

Contact Information for Business Card

One side we would like to have with the general information of the mortuary:
Address: 4127 E. Larkspur Ave, Sun City, AZ 85399
Phone: 623-555-0142
email: hello@willowbendmortuary.example
website: willowbendmortuary.example

On the other side would like to have the information of employee:
Name: Mark T. Ellis
Email: mark@willowbendmortuary.example
Title: Funeral Director
Text: 602-555-0187

Font styles to use
Serif
Sans Serif

Requirements
Should not have
• Do not put any gothic images or things like a hearse or tombstone.

```html
<!DOCTYPE html>
<html lang="en">
<head>
<meta charset="utf-8">
<title>Willowbend Mortuary – Business Card</title>
<link href="https://fonts.googleapis.com/css2?family=Arimo:wght@400;700&family=Poppins:wght@400;600&display=swap" rel="stylesheet">
<style>
  :root {
    --backdrop: #d7d7d7;
    --card: #ffffff;
    --ink: #111111;
    --leaf: #7ac143;
    --leaf-light: #a5d04a;
    --rule: #333333;
  }
  * { box-sizing: border-box; margin: 0; padding: 0; }
  html, body { width: 1200px; height: 800px; overflow: hidden; }
  body { background: var(--backdrop); position: relative; font-family: "Poppins", sans-serif; color: var(--ink); }

  .card { position: absolute; top: 283px; width: 429px; height: 238px; background: var(--card); }
  .card--staff { left: 111px; }
  .card--office { left: 638px; }

  .brand { position: absolute; }
  .brand__mark { position: absolute; width: 46px; height: 46px; border-radius: 50%; background: var(--leaf-light); }
  .brand__name { position: absolute; font-family: "Arimo", sans-serif; font-weight: 700; font-size: 19px; line-height: 21px; letter-spacing: -0.2px; color: var(--ink); white-space: nowrap; }
  .brand__rule { position: absolute; width: 1px; height: 44px; background: var(--leaf); }
  .brand__tagline { position: absolute; font-family: "Arimo", sans-serif; font-size: 12.5px; line-height: 15.5px; color: var(--leaf); }

  .card--staff .brand__mark { left: 88px; top: 60px; }
  .card--staff .brand__name { left: 145px; top: 95px; }
  .card--staff .brand__rule { left: 289px; top: 96px; }
  .card--staff .brand__tagline { left: 292px; top: 96px; }

  .card--office .brand__mark { left: 88px; top: 52px; }
  .card--office .brand__name { left: 143px; top: 91px; }
  .card--office .brand__rule { left: 288px; top: 91px; }
  .card--office .brand__tagline { left: 291px; top: 91px; }

  .identity { position: absolute; right: 270px; text-align: right; font-size: 10.5px; line-height: 13px; }
  .identity__name { font-weight: 600; font-size: 11px; }
  .identity__title { color: var(--leaf-light); font-size: 10px; }
  .address { position: absolute; right: 250px; text-align: right; font-size: 10px; line-height: 14.5px; }

  .divider { position: absolute; width: 1px; background: var(--rule); }

  .contacts { position: absolute; list-style: none; font-size: 10px; line-height: 14px; }
  .contacts li { display: flex; align-items: center; gap: 6px; }
  .contacts svg { width: 8px; height: 8px; fill: var(--leaf); flex: none; }

  .card--staff .identity { top: 183px; }
  .card--staff .divider { left: 174px; top: 184px; height: 23px; }
  .card--staff .contacts { left: 188px; top: 181px; }

  .card--office .address { top: 180px; }
  .card--office .divider { left: 189px; top: 177px; height: 37px; }
  .card--office .contacts { left: 200px; top: 174px; }
</style>
</head>
<body>

<section class="card card--staff" aria-label="Staff side">
  <div class="brand">
    <span class="brand__mark"></span>
    <div class="brand__name">WILLOWBEND<br>MORTUARY</div>
    <span class="brand__rule"></span>
    <div class="brand__tagline">Affordable<br>Cremation<br>and Burial</div>
  </div>
  <div class="identity">
    <div class="identity__name">Mark T. Ellis</div>
    <div class="identity__title">Funeral Director</div>
  </div>
  <span class="divider"></span>
  <ul class="contacts">
    <li><svg viewBox="0 0 24 24"><path d="M6.6 10.8a15.1 15.1 0 0 0 6.6 6.6l2.2-2.2a1 1 0 0 1 1-.25 11.4 11.4 0 0 0 3.6.57 1 1 0 0 1 1 1V20a1 1 0 0 1-1 1A17 17 0 0 1 3 4a1 1 0 0 1 1-1h3.5a1 1 0 0 1 1 1c0 1.25.2 2.45.57 3.57a1 1 0 0 1-.25 1z"/></svg>Text: 602-555-0187</li>
    <li><svg viewBox="0 0 24 24"><path d="M2 5h20v14H2z M3 6l9 7 9-7" fill="none" stroke="#7ac143" stroke-width="0"/><path d="M2 5h20v2l-10 6L2 7z"/><path d="M2 9l10 6 10-6v10H2z"/></svg>mark@willowbendmortuary.example</li>
  </ul>
</section>

<section class="card card--office" aria-label="Office side">
  <div class="brand">
    <span class="brand__mark"></span>
    <div class="brand__name">WILLOWBEND<br>MORTUARY</div>
    <span class="brand__rule"></span>
    <div class="brand__tagline">Affordable<br>Cremation<br>and Burial</div>
  </div>
  <address class="address" style="font-style:normal">
    4127 E. Larkspur Ave<br>Sun City, AZ 85399
  </address>
  <span class="divider"></span>
  <ul class="contacts">
    <li><svg viewBox="0 0 24 24"><path d="M6.6 10.8a15.1 15.1 0 0 0 6.6 6.6l2.2-2.2a1 1 0 0 1 1-.25 11.4 11.4 0 0 0 3.6.57 1 1 0 0 1 1 1V20a1 1 0 0 1-1 1A17 17 0 0 1 3 4a1 1 0 0 1 1-1h3.5a1 1 0 0 1 1 1c0 1.25.2 2.45.57 3.57a1 1 0 0 1-.25 1z"/></svg>623-555-0142</li>
    <li><svg viewBox="0 0 24 24"><path d="M2 5h20v2l-10 6L2 7z"/><path d="M2 9l10 6 10-6v10H2z"/></svg>hello@willowbendmortuary.example</li>
    <li><svg viewBox="0 0 24 24"><path d="M12 2a10 10 0 1 0 0 20 10 10 0 0 0 0-20zm0 2c.9 0 2.2 2 2.7 5H9.3C9.8 6 11.1 4 12 4zM4.3 11h3a20 20 0 0 0 0 2h-3a8 8 0 0 1 0-2zm5 0h5.4a18 18 0 0 1 0 2H9.3a18 18 0 0 1 0-2zm7.4 0h3a8 8 0 0 1 0 2h-3a20 20 0 0 0 0-2zM9.3 15h5.4c-.5 3-1.8 5-2.7 5s-2.2-2-2.7-5z"/></svg>willowbendmortuary.example</li>
  </ul>
</section>

</body>
</html>
```